Video Sharing Site

UPDATE 2: Thanks to everyone who has submitted so far. I have decided to include 2nd and 3rd prizes are well, and I believe with a robust price. If you chose to participate, I will be working with the 2nd and 3rd prize winners also to use your selected designs to complete the rest of the webpages as specified in the brief.

-

UPDATE 1: The key is attractive, SOPHISTICATED yet roomy.

You are free to use any software package you like ie. Joomla, Drupal, Wordpress etc. We just need access to the HTML/CSS.

-

Hello everyone.

We require the HTML/CSS for a video sharing website. Our website is called VidLoomary.com. Think of a unique logo. However this is not the main focus. I will try to give you as much info about the website design as I can:

# Home page:
- with categories in sidebar
- video listings eg. popular, most viewed, etc.
- perhaps make promoted videos stand out

# simple login page

# User Profile page
- user details
- user uploaded videos
- profile comments

# User Profile Edit page

# User Profile Inbox page
- mock messages

# Search page
- list of videos that match search
- number of results
- pagination
- etc.

# Video page
- page where we are watching a video
- related videos
- video comments
- video description
- ratings (thumbs up/down)
- views
- tags
- etc.

# Video Categories page
- list of a few categories eg. newest, most viewed, highest rated, etc.
- with 10-15 videos under each

# Video Upload page with form

# About Us
- with subcategories in sidebar (different design to video categories in home page sidebar)

# Contact Us

# Header
- as any website an attractive search bar should accompany the header
- quick shortlinks to logged-in user eg. (5) comments, (3) inbox, logout, etc.

# Footer
- should be thick so that it can accommodate links to more specific (mock) web pages.

# General
- please be sure to include advertising
- Don't be afraid to use bold colors.
- I will not be selecting designs that are overly dark
- be sure that any page where video thumbnails are shown are accompanied by video rating, number of views and author.
- think about loading times as well. Avoid the use of large graphics where possible.

########### HINT ##########
The first two designs that I pick will be two different types:
- colorful
- quite conservative. Plenty of white with light greys
###########################

Thanks everybody who submits!

2nd and 3rd prized now included!

Just to keep you all updated. I have made a few changes to the brief. Mostly just to make it easier for you to gauge what I'm after.

I have received enough designs with blue in it. Please submit designs where blue is not a main color. Thank you all!

Software

• A sophisticated layout. It must look like a professional video sharing website.

```html
<!DOCTYPE html>
<html lang="en">
<head>
<meta charset="utf-8">
<title>VidLoomary.com – Home</title>
<link href="https://fonts.googleapis.com/css2?family=Noto+Sans:wght@400;700&family=Arimo:wght@400;700&display=swap" rel="stylesheet">
<style>
:root{
  --lime:#b4cc16;
  --lime-bright:#c7e02a;
  --olive:#6a8f12;
  --olive-dark:#4f6d0c;
  --olive-item:#86ad1f;
  --hero-bg:#14181a;
  --page-grey:#f1efef;
  --panel-grey:#efeded;
  --line:#d9d6d6;
  --ink:#1b1b1b;
  --muted:#6d6d6d;
  --star:#e7a414;
  --foot:#34393c;
  --foot-soft:#4a5054;
  --white:#ffffff;
}
*{box-sizing:border-box;margin:0;padding:0}
html,body{width:813px;height:1200px;overflow:hidden}
body{position:relative;background:var(--page-grey);font-family:"Noto Sans",Arial,sans-serif;color:var(--ink)}
.abs{position:absolute}
a{color:inherit;text-decoration:none}

/* top bar */
.topbar{left:0;top:0;width:813px;height:21px;background:var(--lime);font-size:10px;color:#1f2a00}
.topbar .nav{position:absolute;top:4px;display:flex}
.topbar .nav a{padding:0 9px;border-left:1px solid rgba(0,0,0,.2)}
.topbar .nav a:first-child{border-left:0}
.nav-main{left:437px}
.nav-account{right:20px}

/* header */
.header{left:0;top:21px;width:813px;height:119px;background:var(--white)}
.brand{left:36px;top:40px;display:flex;align-items:center;gap:12px}
.brand-dot{width:34px;height:34px;border-radius:50%;background:var(--lime)}
.brand-name{font-size:30px;font-weight:400;color:var(--olive)}
.search{left:410px;top:14px;width:372px;height:28px;border:1px solid #dcdcdc;border-radius:14px;background:#fff;overflow:hidden}
.search span{position:absolute;left:14px;top:7px;font-size:10px;color:#b5b5b5}
.search .go{position:absolute;right:0;top:0;width:35px;height:28px;background:#e6e6dc;border-left:1px solid #d5d5d5}
.ad-banner{left:410px;top:52px;width:372px;height:54px;border:1px dashed #c9c6c6;background:#f6f6f3;border-radius:4px}
.ad-banner span{position:absolute;left:0;top:18px;width:100%;text-align:center;font-size:10px;letter-spacing:1px;color:#9a9a9a;text-transform:uppercase}
.ad-banner small{position:absolute;right:6px;top:3px;font-size:8px;color:#b3b3b3}

/* hero */
.hero{left:0;top:140px;width:813px;height:266px;background:var(--hero-bg)}
.hero-frame{left:35px;top:12px;width:747px;height:241px;border:1px solid #5a6467}
.hero-video{left:3px;top:3px;width:414px;height:233px;background:linear-gradient(100deg,#3a3a3a 0%,#8c1a22 35%,#b3232d 55%,#1e1e1e 80%,#0f0f0f 100%)}
.hero-title{left:452px;top:11px;font-size:19px;color:var(--white)}
.hero-sub{left:453px;top:36px;font-size:13px;color:var(--lime)}
.hero-text{left:454px;top:61px;width:272px;font-size:10.5px;line-height:13px;color:#c9c9c9}
.watch{left:454px;top:127px;width:91px;height:20px;border-radius:3px;background:linear-gradient(#9dd316,#5f9a0a);color:#fff;font-size:11px;font-weight:700;padding:3px 0 0 9px}
.watch svg{position:absolute;right:4px;top:3px}
.dots{right:10px;top:203px;display:flex;gap:6px}
.dots i{width:11px;height:11px;border-radius:50%;background:#8b9296;display:block}
.dots i.on{background:var(--lime)}

/* sidebar */
.sidebar{left:35px;top:414px;width:148px;height:525px;background:var(--olive);border-radius:14px 0 0 14px;border:2px solid #fff;box-shadow:0 0 0 1px var(--line)}
.side-title{left:12px;top:8px;font-size:14.5px;color:#fff}
.cats{left:12px;top:42px;width:126px;list-style:none}
.cats li{height:22px;margin-bottom:2.5px;background:linear-gradient(90deg,var(--olive-item),var(--olive));border-left:3px solid var(--lime-bright);font-size:11px;color:#fff;padding:4px 0 0 9px}
.cats li.on{background:#a0c532}
.cats li.gap{margin-top:6px}
.side-more{right:10px;bottom:8px;font-size:10.5px;color:#fff}

/* main */
.main{left:191px;top:413px;width:591px;height:526px;background:var(--panel-grey);border:1px solid var(--line);border-radius:0 14px 14px 0}
.sec-title{font-size:13px;color:var(--olive)}
.thumb{width:138px}
.thumb .pic{position:relative;width:138px;height:58px;border:2px solid #fff;background:linear-gradient(120deg,#3b3430,#8a6f5f 40%,#d8d3cf 70%,#f4f4f4)}
.thumb .dur{position:absolute;right:2px;top:2px;background:#1a1a1a;color:#fff;font-size:9px;padding:0 3px}
.thumb b{display:block;font-family:"Arimo",Arial,sans-serif;font-weight:400;font-size:10px;margin:6px 0 0 4px;white-space:nowrap}
.thumb small{display:block;font-size:8.5px;color:var(--muted);margin:2px 0 0 4px}
.thumb .stats{display:flex;align-items:center;gap:5px;font-size:8.5px;color:var(--muted);margin:2px 0 0 4px;white-space:nowrap}
.thumb .stars{color:var(--star);letter-spacing:.5px}
.row{display:flex;gap:6.5px}
.see-all{width:56px;height:17px;border-radius:3px;background:linear-gradient(#9dd316,#5f9a0a);color:#fff;font-size:10.5px;padding:1px 0 0 15px}
.see-all::before{content:"";position:absolute;left:6px;top:4px;border:4px solid transparent;border-left:5px solid #fff}
.divider{left:60px;top:178px;width:440px;height:1px;background:linear-gradient(90deg,transparent,#c9c6c6,transparent)}
.spot-head{left:8px;top:385px;font-family:"Arimo",Arial,sans-serif;font-size:11.5px}
.spot-text{left:8px;top:401px;width:265px;font-family:"Arimo",Arial,sans-serif;font-size:9.5px;line-height:13px}
.spot-by{left:8px;top:462px;font-family:"Arimo",Arial,sans-serif;font-size:8.5px;font-weight:700}

/* footer */
.footer{left:0;top:970px;width:813px;height:230px;background:var(--foot)}
.footer-tab{left:35px;top:951px;width:747px;height:40px;background:var(--foot);border-radius:20px 20px 0 0}
.foot-h{font-size:12.5px;color:#fff}
.quick{left:49px;top:1002px;list-style:none}
.quick li{font-size:9.5px;color:var(--lime-bright);height:18.5px}
.quick li::before{content:"";display:inline-block;width:3px;height:3px;background:var(--lime-bright);border-radius:50%;margin:0 8px 2px 0}
.field{left:273px;width:196px;height:20px;background:#fff;border-radius:5px;font-size:8.5px;padding:4px 0 0 9px}
.news-text{left:275px;top:1048px;width:220px;font-size:10px;line-height:12.8px;color:#c9d3a2}
.subscribe{left:273px;top:1120px;width:137px;height:27px;border-radius:4px;background:linear-gradient(#b9dc34,#6f9f0c);border:1px solid #d6ec8a;color:#1f2a00;font-weight:700;font-size:12px;padding:5px 0 0 10px}
.subscribe svg{position:absolute;right:7px;top:4px}
.social{top:996px;display:flex;flex-direction:column;align-items:center;gap:3px;width:50px}
.social i{width:34px;height:34px;border-radius:50%;background:var(--foot-soft);display:block}
.social span{font-size:9px;color:#fff}
.contact-line{left:584px;display:flex;align-items:center;gap:10px;color:#fff}
.copy{left:0;top:1177px;width:813px;text-align:center;font-size:8.5px;color:#d7dadb}
.copy span{padding:0 7px}
</style>
</head>
<body>

<div class="abs topbar">
  <nav class="nav nav-main"><a href="#">Browse</a><a href="#">Movies</a><a href="#">Upload</a></nav>
  <nav class="nav nav-account"><a href="#">Create Account</a><a href="#">Sign In</a></nav>
</div>

<header class="abs header">
  <div class="abs brand"><span class="brand-dot"></span><span class="brand-name">VidLoomary.com</span></div>
  <div class="abs search">
    <span>Search videos</span>
    <div class="go"><svg width="35" height="28" viewBox="0 0 35 28"><circle cx="19" cy="12" r="4.5" fill="none" stroke="#222" stroke-width="2"/><line x1="16" y1="15" x2="12" y2="19" stroke="#222" stroke-width="2.5"/></svg></div>
  </div>
  <div class="abs ad-banner"><small>Ad</small><span>Advertisement</span></div>
</header>

<section class="abs hero">
  <div class="abs hero-frame">
    <div class="abs hero-video" role="img" aria-label="Video still of a child singing at a studio microphone"></div>
    <h1 class="abs hero-title" style="font-weight:400">Why This Melody Loops Again</h1>
    <div class="abs hero-sub">(The Kid Version)</div>
    <p class="abs hero-text">Lorem ipsum dolor sit amet, consectetur adipiscing elit. Cras auctor molestie suscipit. Nulla facilisi.Lorem ipsum dolor sit amet, consectetur adipiscing elit. Cras auctor molestie suscipit. Nulla facilisi.</p>
    <a class="abs watch" href="#">Watch Now<svg width="14" height="14" viewBox="0 0 14 14"><circle cx="7" cy="7" r="6" fill="none" stroke="#fff" stroke-width="1.5"/><path d="M5 4l3 3-3 3" fill="none" stroke="#fff" stroke-width="1.6"/></svg></a>
    <div class="abs dots"><i class="on"></i><i></i><i></i><i></i><i></i></div>
  </div>
</section>

<aside class="abs sidebar">
  <h2 class="abs side-title" style="font-weight:400">Video Categories</h2>
  <ul class="abs cats">
    <li class="on">Trending</li><li>Popular</li><li>Music</li><li>Entertainment</li><li>Sports</li>
    <li class="gap">Film &amp; Animation</li><li>News &amp; Politics</li><li>Comedy</li><li>Science</li><li>Technology</li>
    <li class="gap">Style</li><li>Pets</li><li>Autos</li><li>Travel</li>
    <li class="gap">How To</li><li>Animals</li><li>Vehicles</li><li>Events</li>
  </ul>
  <a class="abs side-more" href="#">&#9656; See All</a>
</aside>

<main class="abs main">
  <h2 class="abs sec-title" style="left:9px;top:12px;font-weight:400">Most Viewed Today</h2>
  <div class="abs row" style="left:8px;top:43px">
    <div class="thumb"><div class="pic" role="img" aria-label="Video thumbnail, two people in a scene"><span class="dur">5.16</span></div><b>Pal Pal Ka Safar Yahan</b><small>Rafa Montero</small><div class="stats"><span class="stars">★★★★☆</span><span>12,480 views</span></div></div>
    <div class="thumb"><div class="pic" role="img" aria-label="Video thumbnail, two people in a scene"><span class="dur">5.16</span></div><b>Pal Pal Ka Safar Yahan</b><small>Rafa Montero</small><div class="stats"><span class="stars">★★★★★</span><span>9,312 views</span></div></div>
    <div class="thumb"><div class="pic" role="img" aria-label="Video thumbnail, two people in a scene"><span class="dur">5.16</span></div><b>Pal Pal Ka Safar Yahan</b><small>Rafa Montero</small><div class="stats"><span class="stars">★★★★☆</span><span>8,054 views</span></div></div>
    <div class="thumb"><div class="pic" role="img" aria-label="Video thumbnail, two people in a scene"><span class="dur">5.16</span></div><b>Pal Pal Ka Safar Yahan</b><small>Rafa Montero</small><div class="stats"><span class="stars">★★★☆☆</span><span>6,720 views</span></div></div>
  </div>
  <a class="abs see-all" href="#" style="left:526px;top:153px">See All</a>
  <div class="abs divider"></div>

  <h2 class="abs sec-title" style="left:9px;top:186px;font-weight:400">Popular Videos</h2>
  <div class="abs row" style="left:8px;top:215px">
    <div class="thumb"><div class="pic" role="img" aria-label="Video thumbnail, two people in a scene"><span class="dur">5.16</span></div><b>Pal Pal Ka Safar Yahan</b><small>Rafa Montero</small><div class="stats"><span class="stars">★★★★★</span><span>41,205 views</span></div></div>
    <div class="thumb"><div class="pic" role="img" aria-label="Video thumbnail, two people in a scene"><span class="dur">5.16</span></div><b>Pal Pal Ka Safar Yahan</b><small>Rafa Montero</small><div class="stats"><span class="stars">★★★★☆</span><span>38,910 views</span></div></div>
    <div class="thumb"><div class="pic" role="img" aria-label="Video thumbnail, two people in a scene"><span class="dur">5.16</span></div><b>Pal Pal Ka Safar Yahan</b><small>Rafa Montero</small><div class="stats"><span class="stars">★★★★☆</span><span>35,466 views</span></div></div>
    <div class="thumb"><div class="pic" role="img" aria-label="Video thumbnail, two people in a scene"><span class="dur">5.16</span></div><b>Pal Pal Ka Safar Yahan</b><small>Rafa Montero</small><div class="stats"><span class="stars">★★★★★</span><span>33,018 views</span></div></div>
  </div>
  <a class="abs see-all" href="#" style="left:526px;top:325px">See All</a>

  <h2 class="abs sec-title" style="left:9px;top:356px;font-weight:400">Spotlight</h2>
  <div class="abs spot-head">Best Of Bollywood Hits: 2011</div>
  <p class="abs spot-text">From the beats of Tinka Tunka to the madness of Dhoom Zara Zor - 2011 saw it all! Here's VidLoomary's biggest Bollywood Hits for all music lovers out there! Lets sing and dance goodbye to a great year with VidLoomary!</p>
  <div class="abs spot-by">Presented By : Leo Brandt</div>
  <div class="abs row" style="left:283px;top:385px;gap:15px">
    <div class="thumb"><div class="pic" role="img" aria-label="Video thumbnail, two people in a scene"><span class="dur">5.16</span></div><b>Pal Pal Ka Safar Yahan</b><small>Rafa Montero</small><div class="stats"><span class="stars">★★★★☆</span><span>22,637 views</span></div></div>
    <div class="thumb"><div class="pic" role="img" aria-label="Video thumbnail, two people in a scene"><span class="dur">5.16</span></div><b>Pal Pal Ka Safar Yahan</b><small>Rafa Montero</small><div class="stats"><span class="stars">★★★★★</span><span>19,804 views</span></div></div>
  </div>
  <a class="abs see-all" href="#" style="left:526px;top:499px">See All</a>
</main>

<div class="abs footer-tab"></div>
<footer class="abs footer"></footer>

<h3 class="abs foot-h" style="left:49px;top:968px;font-weight:400">Quick Links</h3>
<ul class="abs quick">
  <li>Home</li><li>Browse</li><li>Movies</li><li>Upload</li><li>Profile</li><li>Contact Us</li>
</ul>

<h3 class="abs foot-h" style="left:272px;top:971px;font-weight:400">Subscribe Newsletters</h3>
<div class="abs field" style="top:994px">Your name</div>
<div class="abs field" style="top:1021px">Your email id</div>
<p class="abs news-text">Lorem ipsum dolor sit amet, consectetur adipiscing elit. Proin posuere ipsum sit amet urna bibendum iaculis. Etiam faucibus ultricies diam ac facilisis. Maecenas eleifend iaculis vulputate.</p>
<a class="abs subscribe" href="#">SUBSCRIBE NOW<svg width="18" height="18" viewBox="0 0 18 18"><circle cx="9" cy="9" r="7.5" fill="#fff" stroke="#5f8a0a"/><path d="M7 5l4 4-4 4" fill="none" stroke="#5f8a0a" stroke-width="1.8"/></svg></a>

<h3 class="abs foot-h" style="left:581px;top:971px;font-weight:400">Follow Us</h3>
<div class="abs social" style="left:577px"><i></i><span>Friendly</span></div>
<div class="abs social" style="left:638px"><i></i><span>Chirpr</span></div>
<div class="abs social" style="left:698px"><i></i><span>Blogsy</span></div>

<h3 class="abs foot-h" style="left:583px;top:1057px;font-weight:400">Contact Us</h3>
<div class="abs contact-line" style="top:1080px;font-size:14px">
  <svg width="20" height="20" viewBox="0 0 20 20"><path d="M5 2c1 0 2 3 2 4s-2 1-1.5 2.5 3 5 5 5.5c1 .3 1.5-1.5 2.5-1.5s4 1.5 4 2.5-2 3-3.5 3C8 18 2 11 2 5.5 2 4 4 2 5 2z" fill="#e63a2a"/></svg>
  <span>555 0142 789</span>
</div>
<div class="abs contact-line" style="top:1117px;font-size:11.5px">
  <svg width="22" height="18" viewBox="0 0 22 18"><rect x="2" y="3" width="16" height="11" rx="2" fill="#8cc63f"/><path d="M2 4l8 6 8-6" fill="none" stroke="#fff" stroke-width="1.3"/></svg>
  <span>info@vidloomary.com</span>
</div>

<div class="abs copy"><span>© 2011, All Rights Reserved, Privacy Policy</span>|<span>Terms &amp; Conditions</span>|<span>Sitemap</span></div>

</body>
</html>
```